Velmora Biz Card 2019

New business card for Velmora Property Inspections. We are a residential home inspection company in Arizona.

Target Market(s)

Real Estate

Font styles to use
Sans Serif

Requirements
Must have
• Glen Mirewick
• Home Inspector
• Velmora Property Inspections, LLC
• 480-555-0172
• glen@velmora-llc.example

```html
<!DOCTYPE html>
<html lang="en">
<head>
<meta charset="utf-8">
<title>Velmora Property Inspections – Business Card</title>
<link rel="stylesheet" href="https://fonts.googleapis.com/css2?family=Montserrat:wght@500;600;700;800&display=swap">
<style>
  :root {
    --stage: #2a2b2e;
    --card-white: #ffffff;
    --back-grey: #6a6b6d;
    --back-grey-light: #77787a;
    --emboss-dark: #4f5052;
    --ink-grey: #5a5b5d;
    --band-grey: #4a4b4d;
    --accent-green: #45b649;
    --rule-grey: #8a8b8d;
    --navy: #232a3a;
  }
  * { margin: 0; padding: 0; box-sizing: border-box; }
  html, body {
    width: 1200px; height: 800px; overflow: hidden;
    background: var(--stage);
    font-family: "Montserrat", Arial, sans-serif;
  }
  .stage {
    position: relative; width: 1200px; height: 800px;
    display: flex; align-items: center; justify-content: center; gap: 40px;
  }
  .card {
    position: relative; width: 540px; height: 309px; overflow: hidden;
    box-shadow: 0 14px 30px rgba(0,0,0,0.45);
  }

  /* Back */
  .card-back {
    background: linear-gradient(135deg, var(--back-grey-light) 0%, var(--back-grey) 60%, #616264 100%);
  }
  .card-back .brand-mark {
    position: absolute; right: 56px; top: 92px;
    display: flex; align-items: center; gap: 12px;
  }
  .card-back .brand-square {
    width: 26px; height: 26px; background: var(--emboss-dark);
  }
  .card-back .brand-name {
    font-weight: 800; font-size: 40px; letter-spacing: 1px;
    color: var(--emboss-dark);
  }

  /* Front */
  .card-front { background: var(--card-white); }
  .portrait {
    position: absolute; right: 0; top: 0; width: 240px; height: 262px;
    background: linear-gradient(180deg, #ffffff 0%, #f1ebe6 30%, #c9a58f 55%, var(--navy) 85%);
  }
  .bottom-band {
    position: absolute; left: 0; bottom: 0; width: 100%; height: 48px;
    background: var(--band-grey);
  }
  .corner-accent { position: absolute; right: 0; bottom: 40px; }
  .brand-name-front {
    position: absolute; left: 30px; top: 108px;
    font-weight: 800; font-size: 36px; letter-spacing: 1px; line-height: 1;
    color: var(--ink-grey);
  }
  .divider {
    position: absolute; left: 30px; top: 158px; width: 240px; height: 1px;
    background: var(--rule-grey);
  }
  .identity {
    position: absolute; left: 30px; top: 168px;
    font-size: 12.5px; font-weight: 700; color: var(--ink-grey);
    display: flex; align-items: center; gap: 7px; white-space: nowrap;
  }
  .identity .role { color: var(--accent-green); font-weight: 600; }
  .identity .sep { font-weight: 500; color: var(--rule-grey); }
  .contacts {
    position: absolute; left: 30px; top: 198px; list-style: none;
    font-size: 11.5px; font-weight: 500; color: var(--ink-grey);
  }
  .contacts li { display: flex; align-items: center; gap: 8px; height: 21px; white-space: nowrap; }
  .contacts svg { width: 15px; height: 15px; flex: none; }
  .website {
    position: absolute; left: 30px; bottom: 16px;
    font-size: 12px; font-weight: 500; letter-spacing: 3px; color: #ffffff;
  }
</style>
</head>
<body>
<main class="stage">

  <section class="card card-back" aria-label="Card back">
    <div class="brand-mark">
      <span class="brand-square"></span>
      <span class="brand-name">VELMORA</span>
    </div>
  </section>

  <section class="card card-front" aria-label="Card front">
    <div class="portrait" role="img" aria-label="Portrait photograph of Glen Mirewick"></div>
    <svg class="corner-accent" width="110" height="80" viewBox="0 0 110 80" aria-hidden="true">
      <polygon points="40,80 110,80 110,0 84,10" fill="var(--accent-green)"/>
      <polygon points="26,80 40,80 84,10 78,12" fill="#ffffff"/>
    </svg>
    <div class="bottom-band"></div>

    <div class="brand-name-front">VELMORA</div>
    <div class="divider"></div>
    <div class="identity">
      <span class="name">GLEN MIREWICK</span>
      <span class="sep">|</span>
      <span class="role">Home Inspector</span>
    </div>
    <ul class="contacts">
      <li>
        <svg viewBox="0 0 16 16" aria-hidden="true">
          <circle cx="8" cy="8" r="7" fill="none" stroke="var(--accent-green)" stroke-width="1.4"/>
          <rect x="5.5" y="4" width="5" height="8" rx="1" fill="none" stroke="var(--accent-green)" stroke-width="1.2"/>
        </svg>
        <span>480-555-0172</span>
      </li>
      <li>
        <svg viewBox="0 0 16 16" aria-hidden="true">
          <circle cx="8" cy="8" r="7" fill="var(--accent-green)"/>
          <rect x="4.2" y="5.2" width="7.6" height="5.6" fill="#ffffff"/>
          <polyline points="4.2,5.2 8,8.4 11.8,5.2" fill="none" stroke="var(--accent-green)" stroke-width="1"/>
        </svg>
        <span>glen@velmora-llc.example</span>
      </li>
    </ul>
    <div class="website">www.velmora-llc.example</div>
  </section>

</main>
</body>
</html>
```